Insurance company needs a business card design

We need a business card design for a Massachusetts-based insurance company Veloria Insurance, LLC. We provide auto insurance to Hispanic (Spanish- or Portuguese-speaking) immigrants in the United States. We will give these business cards to auto dealers where such customers typically go to purchase vehicles. We will provide a solution to the dealers to provide easy insurance to the customers buying cars at their dealerships. Veloria is the Spanish word for protection.
Contact Information for Business Card
Name, Designation, Company Name, Address, Phone Number, Email, Website
Look and feel
Each slider illustrates characteristics of the customer's brand and the style your logo design should communicate.

```html
<!DOCTYPE html>
<html lang="en">
<head>
<meta charset="utf-8">
<title>Veloria Insurance – Business Card</title>
<link rel="stylesheet" href="https://fonts.googleapis.com/css2?family=Lato:wght@400;700&family=Montserrat:wght@800&display=swap">
<style>
  :root {
    --navy: #004a7c;
    --orange: #f08700;
    --white: #ffffff;
    --ink: #1f1f1f;
    --stage: #1c1c1c;
  }
  * { margin: 0; padding: 0; box-sizing: border-box; }
  html, body { width: 1200px; height: 901px; overflow: hidden; }
  body {
    background: var(--stage);
    font-family: "Lato", sans-serif;
    position: relative;
  }
  .card {
    position: absolute;
    top: 296px;
    width: 540px;
    height: 309px;
    overflow: hidden;
  }
  .card-front { left: 40px; background: var(--navy); }
  .card-back { left: 620px; background: var(--white); }

  /* front */
  .front-brand {
    position: absolute;
    left: 0; right: 0; top: 112px;
    text-align: center;
    color: var(--white);
    font-weight: 700;
    font-size: 40px;
    letter-spacing: 1px;
    text-transform: uppercase;
  }
  .front-brand-mark {
    display: inline-block;
    width: 18px; height: 18px;
    background: var(--orange);
    border-radius: 50%;
    margin-right: 14px;
    vertical-align: 4px;
  }
  .front-url {
    position: absolute;
    left: 0; right: 0; bottom: 42px;
    text-align: center;
    color: var(--white);
    font-size: 14px;
    letter-spacing: 0.5px;
  }

  /* back */
  .back-rule {
    position: absolute;
    left: 0; right: 0; bottom: 38px;
    height: 4px;
    background: var(--orange);
  }
  .back-band {
    position: absolute;
    left: 0; right: 0; bottom: 0;
    height: 38px;
    background: var(--navy);
  }
  .back-brand {
    position: absolute;
    left: 30px; top: 108px;
    width: 180px;
    text-align: center;
    color: var(--navy);
    font-weight: 700;
    font-size: 34px;
  }
  .back-divider {
    position: absolute;
    left: 228px; top: 56px;
    width: 2px; height: 148px;
    background: var(--navy);
  }
  .contact {
    position: absolute;
    left: 252px; top: 50px;
    color: var(--ink);
  }
  .contact-name {
    font-family: "Montserrat", sans-serif;
    font-weight: 800;
    font-size: 21px;
    color: var(--navy);
    line-height: 1;
  }
  .contact-title {
    color: var(--orange);
    font-size: 14px;
    margin-top: 2px;
  }
  .contact-address {
    font-size: 12.5px;
    line-height: 1.4;
    margin-top: 10px;
  }
  .contact-list { list-style: none; margin-top: 8px; font-size: 12.5px; }
  .contact-list li { display: flex; align-items: center; gap: 8px; line-height: 1.55; }
  .contact-icon { width: 12px; height: 12px; flex: none; }
</style>
</head>
<body>
  <section class="card card-front" aria-label="Card front">
    <div class="front-brand"><span class="front-brand-mark"></span>Veloria Insurance</div>
    <div class="front-url">www.veloriains.com</div>
  </section>

  <section class="card card-back" aria-label="Card back">
    <div class="back-rule"></div>
    <div class="back-band"></div>

    <div class="back-brand">Veloria</div>
    <div class="back-divider"></div>

    <div class="contact">
      <div class="contact-name">DANIEL REYES</div>
      <div class="contact-title">President</div>
      <div class="contact-address">418 Harbor View Road<br>Suite 210 Lowell, MA 01852</div>
      <ul class="contact-list">
        <li>
          <svg class="contact-icon" viewBox="0 0 12 12"><path d="M2.5 1 L4.5 1 L5.2 3.6 L4 4.6 C4.7 6 5.9 7.3 7.4 8 L8.4 6.8 L11 7.5 L11 9.5 C11 10.3 10.3 11 9.5 11 C5 11 1 7 1 2.5 C1 1.7 1.7 1 2.5 1 Z" fill="var(--orange)"/></svg>
          +1 978 555 0142
        </li>
        <li>
          <svg class="contact-icon" viewBox="0 0 12 12"><rect x="0.5" y="2" width="11" height="8" fill="var(--orange)"/><path d="M0.5 2 L6 6.5 L11.5 2" stroke="var(--white)" stroke-width="1" fill="none"/></svg>
          hello@veloriains.com
        </li>
        <li>
          <svg class="contact-icon" viewBox="0 0 12 12"><circle cx="6" cy="6" r="5.5" fill="var(--orange)"/><path d="M0.5 6 H11.5 M6 0.5 C3.5 3 3.5 9 6 11.5 M6 0.5 C8.5 3 8.5 9 6 11.5" stroke="var(--white)" stroke-width="0.8" fill="none"/></svg>
          www.veloriains.com
        </li>
      </ul>
    </div>
  </section>
</body>
</html>
```